Hillcrest BBQ Co. Rub and Sauce Labels

I am bringing to market 3 different meat rubs and 2 BBQ sauces. These rubs and sauces will be sold on an eCommerce website and also at local events. I am looking for simplicity. I believe the BBQ seasoning labels out there are very busy. I am looking for each label to be similar, yet distinct enough to clearly differentiate the different rubs in my offerings. My logo is attached. The Smoky H in my logo is going to be a feature in my brand and would like to have it be a feature on my labels, too. The rubs will be packaged in a traditional clear plastic shaker with a pop-top. I am open to ideas on packaging options as well. The different rubs in the shakers will range in color from very light to dark brown, depending on the ingredients in each rub. Please include all FDA required information on the labels. The rub labels will go on a clear plastic shaker and the sauce will be packaged in a bottle. Thanks for your help and I look forward to seeing your creativity come to life!

Colors

Designer to choose colors to be used in the design.

Requirements
Must have
• Simplicity, yet ability to separate multiple products by simple changes in logo and/or packaging. Please see the attached photo of a competitors bbq sauce - something simple yet flexible.
Nice to have
• Flexibility in design.

```html
<!DOCTYPE html>
<html lang="en">
<head>
<meta charset="utf-8">
<title>Hillcrest BBQ Co. – Rub and Sauce Labels</title>
<link rel="stylesheet" href="https://fonts.googleapis.com/css2?family=Archivo+Black&family=Archivo:wght@700&display=swap">
<style>
  :root {
    --page-bg: #ffffff;
    --label-bg: #464342;
    --label-text: #ffffff;
    --accent: #f06a1d;
  }
  html, body {
    margin: 0;
    padding: 0;
    overflow: hidden;
  }
  body {
    width: 1200px;
    height: 1000px;
    background: var(--page-bg);
    position: relative;
  }
  .label {
    position: absolute;
    background: var(--label-bg);
    color: var(--label-text);
  }
  .label--rub {
    left: 298px;
    top: 553px;
    width: 180px;
    height: 293px;
  }
  .label--sauce {
    left: 577px;
    top: 582px;
    width: 245px;
    height: 278px;
    border-radius: 4px;
  }
  .product-name {
    position: absolute;
    margin: 0;
    writing-mode: vertical-rl;
    transform: rotate(180deg);
    font-family: "Archivo Black", sans-serif;
    font-weight: 400;
    text-transform: uppercase;
    letter-spacing: 1px;
  }
  .label--rub .product-name {
    right: 10px;
    top: 22px;
    height: 186px;
    font-size: 54px;
    line-height: 0.86;
  }
  .label--sauce .product-name {
    right: 62px;
    top: 22px;
    height: 176px;
    font-size: 46px;
    line-height: 0.92;
  }
  .brand {
    position: absolute;
    display: flex;
    align-items: center;
    gap: 6px;
  }
  .label--rub .brand { left: 20px; top: 214px; }
  .label--sauce .brand { left: 60px; top: 196px; }
  .brand__dot {
    width: 24px;
    height: 24px;
    border-radius: 50%;
    background: var(--accent);
    flex: none;
  }
  .brand__name {
    font-family: "Archivo", sans-serif;
    font-weight: 700;
    font-size: 11px;
    color: var(--label-text);
    white-space: nowrap;
  }
  .net-weight {
    position: absolute;
    margin: 0;
    font-family: "Archivo", sans-serif;
    font-weight: 700;
    font-size: 6px;
    line-height: 8px;
    text-align: center;
    white-space: nowrap;
    color: var(--label-text);
  }
  .label--rub .net-weight { top: 279px; left: 34px; right: 0; }
  .label--sauce .net-weight { top: 265px; left: 0; right: 0; }
</style>
</head>
<body>
  <section class="label label--rub">
    <h1 class="product-name">Meat<br>Rub</h1>
    <div class="brand">
      <span class="brand__dot"></span>
      <span class="brand__name">HILLCREST BBQ CO.</span>
    </div>
    <p class="net-weight">NET WT. 18 OZ (1LB 2 OZ) 510g</p>
  </section>

  <section class="label label--sauce">
    <h1 class="product-name">BBQ<br>Sauce</h1>
    <div class="brand">
      <span class="brand__dot"></span>
      <span class="brand__name">HILLCREST BBQ CO.</span>
    </div>
    <p class="net-weight">NET WT. 18 OZ (1LB 2 OZ) 510g</p>
  </section>
</body>
</html>
```